Marchesi Orthodontics
Business Card / Stationary Design
Professional
Lucia Marchesi
Orthodontist
4817 W. Harborview Ave. Suite 204
Pine Grove, SC 33419
marchesiortho@mailvexo.com
www.pinegrovesmiles.com

```html
<!DOCTYPE html>
<html lang="en">
<head>
<meta charset="utf-8">
<title>Marchesi Orthodontics — Stationery</title>
<link href="https://fonts.googleapis.com/css2?family=Exo+2:wght@400;600&display=swap" rel="stylesheet">
<style>
  :root{
    --bg:#e9eaec;
    --paper:#ffffff;
    --blue:#1f7fcf;
    --blue-dark:#0f4f92;
    --blue-light:#5fb2ee;
    --ink:#3b4452;
    --muted:#8a93a0;
    --black:#121315;
    --silver-1:#d9dbde;
    --silver-2:#9da1a7;
    --faint:#e4eef8;
  }
  *{box-sizing:border-box;margin:0;padding:0}
  html,body{width:1200px;height:497px;overflow:hidden;background:var(--bg)}
  body{position:relative;font-family:"Exo 2",sans-serif;color:var(--ink)}
  .sheet{position:absolute;overflow:hidden;background:var(--paper);box-shadow:0 2px 6px rgba(0,0,0,.25)}
  .logo{position:absolute;display:flex;align-items:center;gap:4px;font-weight:600;color:var(--blue);white-space:nowrap;letter-spacing:.04em}
  .logo .dot{width:.9em;height:.9em;border-radius:50%;background:currentColor}
  .logo.on-dark{color:#ffffff}
  .contact{position:absolute;font-size:5.5px;line-height:1.45;color:var(--ink);white-space:nowrap}
  .faint-circle{position:absolute;border-radius:50%;background:var(--faint)}
  .wave{position:absolute;display:block}

  /* business cards */
  .card{width:204px;height:78px}
  .card-1{left:8px;top:24px}
  .card-2{left:221px;top:24px}
  .card-3{left:8px;top:113px}
  .card-4{left:221px;top:113px;background:var(--black)}
  .card-5{left:8px;top:202px;background:linear-gradient(135deg,var(--blue-light),var(--blue-dark))}
  .card-6{left:221px;top:202px;background:linear-gradient(135deg,var(--silver-1),var(--silver-2))}
  .card .person{position:absolute;font-size:7px;font-weight:600;color:#fff;text-align:right}
  .card .person small{display:block;font-size:5px;font-weight:400}
  .card .url{position:absolute;left:0;right:0;bottom:8px;text-align:center;font-size:5px;color:var(--muted)}
  .card-4 .url,.card-5 .url{color:#dfe8f2}
  .card-6 .url{color:#4d525a}

  /* letterhead */
  .letterhead{left:432px;top:22px;width:214px;height:280px}

  /* envelopes */
  .envelope-back{width:468px;height:170px;background:#f7f8f9}
  .envelope-back.rear{left:720px;top:22px}
  .envelope-back.middle{left:700px;top:76px;height:150px}
  .flap{position:absolute;left:0;top:0;width:100%;height:100%}
  .envelope-front{left:660px;top:178px;width:480px;height:278px}
</style>
</head>
<body>

<!-- Business card 1: front with blue swoosh -->
<section class="sheet card card-1" aria-label="Business card front">
  <svg class="wave" width="204" height="78" viewBox="0 0 204 78" aria-hidden="true">
    <path d="M150 0 Q120 40 170 78 L204 78 L204 0Z" fill="var(--blue)"/>
    <path d="M140 0 Q112 40 160 78 L168 78 Q122 40 150 0Z" fill="var(--blue-light)"/>
  </svg>
  <div class="logo" style="left:8px;top:8px;font-size:8px">Marchesi Orthodontics<span class="dot"></span></div>
  <div class="contact" style="left:8px;top:36px">
    4817 W. Harborview Ave. Suite 204<br>Pine Grove, SC 33419<br>(954) 555-0142<br>marchesiortho@mailvexo.com
  </div>
</section>

<!-- Business card 2: back with name panel -->
<section class="sheet card card-2" aria-label="Business card back">
  <svg class="wave" width="204" height="78" viewBox="0 0 204 78" aria-hidden="true">
    <path d="M120 0 Q100 40 130 78 L204 78 L204 0Z" fill="var(--blue)"/>
  </svg>
  <div class="contact" style="left:8px;top:8px">
    4817 W. Harborview Ave. Suite 204<br>Pine Grove, SC 33419<br>P (954) 555-0142<br>F (954) 555-0187<br>marchesiortho@mailvexo.com<br>www.pinegrovesmiles.com
  </div>
  <div class="person" style="right:10px;top:30px">Lucia Marchesi<small>Orthodontist</small></div>
</section>

<!-- Business card 3: white logo card -->
<section class="sheet card card-3" aria-label="Business card, white">
  <div class="faint-circle" style="left:120px;top:4px;width:70px;height:70px"></div>
  <div class="logo" style="left:12px;top:30px;font-size:10px">Marchesi Orthodontics<span class="dot"></span></div>
  <div class="url">www.pinegrovesmiles.com</div>
</section>

<!-- Business card 4: black -->
<section class="sheet card card-4" aria-label="Business card, black">
  <div class="logo on-dark" style="left:30px;top:30px;font-size:10px">Marchesi Orthodontics<span class="dot"></span></div>
  <div class="url">www.pinegrovesmiles.com</div>
</section>

<!-- Business card 5: blue -->
<section class="sheet card card-5" aria-label="Business card, blue">
  <div class="faint-circle" style="left:118px;top:4px;width:70px;height:70px;background:rgba(255,255,255,.15)"></div>
  <div class="logo on-dark" style="left:12px;top:30px;font-size:10px">Marchesi Orthodontics<span class="dot"></span></div>
  <div class="url">www.pinegrovesmiles.com</div>
</section>

<!-- Business card 6: silver -->
<section class="sheet card card-6" aria-label="Business card, silver">
  <div class="logo" style="left:30px;top:30px;font-size:10px;color:var(--black)">Marchesi Orthodontics<span class="dot"></span></div>
  <div class="url">www.pinegrovesmiles.com</div>
</section>

<!-- Letterhead -->
<section class="sheet letterhead" aria-label="Letterhead">
  <div class="faint-circle" style="left:18px;top:70px;width:150px;height:150px"></div>
  <svg class="wave" width="214" height="280" viewBox="0 0 214 280" aria-hidden="true" style="left:0;top:0">
    <path d="M214 60 Q190 170 214 280Z" fill="var(--blue)"/>
    <path d="M206 120 Q196 200 214 280 L210 280 Q190 200 206 120Z" fill="var(--blue-light)"/>
  </svg>
  <div class="logo" style="left:10px;top:13px;font-size:7.5px">Marchesi Orthodontics<span class="dot"></span></div>
  <div class="contact" style="left:126px;top:8px;font-size:5px">
    4817 W. Harborview Ave. Suite 204<br>Pine Grove, SC 33419<br>P (954) 555-0142<br>F (954) 555-0187<br>marchesiortho@mailvexo.com<br>www.pinegrovesmiles.com
  </div>
</section>

<!-- Envelope backs -->
<section class="sheet envelope-back rear" aria-label="Envelope back">
  <svg class="flap" viewBox="0 0 468 170" preserveAspectRatio="none" aria-hidden="true">
    <defs>
      <linearGradient id="flapGrey" x1="0" y1="0" x2="0" y2="1">
        <stop offset="0" stop-color="#7e848c"/><stop offset="1" stop-color="#c9ccd0"/>
      </linearGradient>
    </defs>
    <path d="M0 0 L468 0 L468 20 Q234 100 0 20Z" fill="url(#flapGrey)"/>
  </svg>
  <div class="faint-circle" style="left:212px;top:6px;width:42px;height:42px;background:rgba(255,255,255,.55)"></div>
</section>

<section class="sheet envelope-back middle" aria-label="Envelope back, open flap">
  <svg class="flap" viewBox="0 0 468 150" preserveAspectRatio="none" aria-hidden="true">
    <path d="M0 0 L234 70 L468 0" fill="none" stroke="#d5d8dc" stroke-width="1.5"/>
  </svg>
</section>

<!-- Envelope front -->
<section class="sheet envelope-front" aria-label="Envelope front">
  <svg class="wave" width="480" height="278" viewBox="0 0 480 278" aria-hidden="true">
    <defs>
      <linearGradient id="bandBlue" x1="0" y1="0" x2="1" y2="0">
        <stop offset="0" stop-color="var(--blue-dark)"/><stop offset="1" stop-color="var(--blue-light)"/>
      </linearGradient>
    </defs>
    <path d="M0 0 L480 0 L480 30 Q240 70 0 40Z" fill="url(#bandBlue)"/>
    <path d="M0 46 Q240 78 480 36 L480 40 Q240 84 0 50Z" fill="var(--blue-light)"/>
  </svg>
  <div class="faint-circle" style="left:300px;top:70px;width:170px;height:170px"></div>
  <div class="logo" style="left:22px;top:66px;font-size:12px">Marchesi Orthodontics<span class="dot"></span></div>
  <div class="contact" style="left:22px;top:226px;font-size:6.5px">
    4817 W. Harborview Ave. Suite 204<br>Pine Grove, SC 33419<br>www.pinegrovesmiles.com
  </div>
</section>

</body>
</html>
```